Business Card for Coach - ready to print

Design Business Card ready to order prints www.lukasbrenner.coach

* An Overview / Background of the Business & Services
· Coaching
· Personal growth
* The Target Market / Audience you are trying to reach
· private person in different roles (self, familiy, business role)s
* Design Specifics; any preferences or ideas for Style, Colour, Imagery, etc
· See www.lukasbrenner.coach
· "simple" design
· (small) element of surprise / unusual element

* Information that will be placed in the Business Card
· Beratung und Coaching
· Address: Lukas Brenner, Talmatt 42, CH-8531 Winterthur, Mobile +41 76 254 63 07
* Do you have an existing website or Facebook page where designers can learn more about your company?
· lukasbrenner.coach

Target Market(s)

private person in different roles (self, familiy, business role)

Industry/Entity Type

Life Coaching

Contact Information for Business Card

Lukas Brenner
Talmatt 42
CH-8531 Winterthur

Mobile: +41 76 254 63 07
Email: lubr@sonnwelt.ch
www.lukasbrenner.coach

Font styles to use
Sans Serif

Colors

Designer to choose colors to be used in the design.

Requirements
Must have
• "simple" design
• element of surprise / unusual element
• Beratung & Coaching
• see www.lukasbrenner.coach for colors and so...
Nice to have
• TA Symbol (three rings on top of each other) - unsual presentation
• QR Code of Website (see if it fits in and still looks good).

```html
<!DOCTYPE html>
<html lang="de">
<head>
<meta charset="utf-8">
<title>Lukas Brenner – Visitenkarte</title>
<link rel="stylesheet" href="https://fonts.googleapis.com/css2?family=Montserrat:wght@400;500;600;700&display=swap">
<style>
  :root {
    --backdrop: #eceded;
    --card: #a9a9aa;
    --accent: #1f7fbf;
    --accent-soft: #7fc3ee;
    --ink: #1c3550;
    --divider: #7a7b7d;
    --white: #ffffff;
  }
  * { box-sizing: border-box; margin: 0; padding: 0; }
  html, body {
    width: 1200px; height: 900px; overflow: hidden;
    background: var(--backdrop);
    font-family: "Montserrat", Arial, sans-serif;
  }
  .sheet {
    width: 1200px; height: 900px;
    display: flex; flex-direction: column; align-items: center; justify-content: center;
    gap: 30px;
  }
  .card {
    width: 740px; height: 410px;
    background: var(--card);
    box-shadow: 0 6px 18px rgba(0,0,0,0.12);
    position: relative;
  }

  /* Front */
  .card-front { display: flex; align-items: center; }
  .portrait {
    position: absolute; left: 125px; top: 120px;
    width: 170px; height: 170px; border-radius: 50%;
    background: radial-gradient(circle at 50% 38%, #c49a7a 0 18%, #8d9aa8 19% 46%, #4b5566 47% 100%);
  }
  .divider {
    position: absolute; left: 365px; top: 110px;
    width: 2px; height: 195px; background: var(--divider);
  }
  .contact { position: absolute; left: 438px; top: 118px; }
  .contact-name {
    color: var(--accent); font-weight: 600; font-size: 25px; letter-spacing: 1px;
    margin-bottom: 36px;
  }
  .contact-row {
    display: flex; align-items: flex-start; gap: 9px;
    color: var(--accent); font-size: 17px; letter-spacing: 1px; line-height: 22px;
    margin-bottom: 17px;
  }
  .contact-row svg { flex: none; width: 16px; height: 18px; margin-top: 2px; fill: var(--ink); }

  /* Back */
  .card-back { display: flex; flex-direction: column; align-items: center; }
  .offer-title {
    margin-top: 62px;
    color: var(--ink); font-weight: 700; font-size: 15px; letter-spacing: 1.5px;
    text-decoration: underline; text-underline-offset: 4px;
  }
  .services {
    margin-top: 60px; width: 640px;
    display: flex; justify-content: space-between;
  }
  .service { width: 210px; display: flex; flex-direction: column; align-items: center; gap: 14px; }
  .service-icon {
    width: 44px; height: 34px; border-radius: 50%;
    background: var(--accent-soft);
    display: flex; align-items: center; justify-content: center;
  }
  .service-icon svg { width: 20px; height: 20px; fill: none; stroke: var(--white); stroke-width: 2.2; }
  .service-label { color: var(--ink); font-size: 13px; letter-spacing: 0.5px; }
  .website {
    position: absolute; bottom: 58px; left: 0; right: 0; text-align: center;
    color: var(--ink); font-weight: 600; font-size: 14px; letter-spacing: 0.8px;
  }
</style>
</head>
<body>
<main class="sheet">
  <section class="card card-front" aria-label="Vorderseite">
    <div class="portrait" role="img" aria-label="Porträtfoto von Lukas Brenner"></div>
    <div class="divider"></div>
    <div class="contact">
      <h1 class="contact-name">Lukas Brenner</h1>
      <p class="contact-row">
        <svg viewBox="0 0 16 18" aria-hidden="true"><path d="M4 0h8a2 2 0 0 1 2 2v14a2 2 0 0 1-2 2H4a2 2 0 0 1-2-2V2a2 2 0 0 1 2-2zm0 2v12h8V2zm4 13a1 1 0 1 0 0 2 1 1 0 0 0 0-2z"/></svg>
        <span>+41 76 254 63 07</span>
      </p>
      <p class="contact-row">
        <svg viewBox="0 0 16 18" aria-hidden="true"><path d="M0 4h16v11H0zm1.5 1.5L8 10l6.5-4.5V5h-13z"/></svg>
        <span>lubr@sonnwelt.ch</span>
      </p>
      <p class="contact-row">
        <svg viewBox="0 0 16 18" aria-hidden="true"><path d="M8 0a6 6 0 0 1 6 6c0 4.5-6 12-6 12S2 10.5 2 6a6 6 0 0 1 6-6zm0 3.5a2.5 2.5 0 1 0 0 5 2.5 2.5 0 0 0 0-5z"/></svg>
        <span>Talmatt 42<br>CH-8531 Winterthur</span>
      </p>
    </div>
  </section>

  <section class="card card-back" aria-label="Rückseite">
    <h2 class="offer-title">MEIN ANGEBOT</h2>
    <div class="services">
      <div class="service">
        <span class="service-icon"><svg viewBox="0 0 20 20" aria-hidden="true"><path d="M16 10a6 6 0 1 1-2-4.5"/><path d="M14 2v4h-4"/></svg></span>
        <span class="service-label">Beratung &amp; Coaching</span>
      </div>
      <div class="service">
        <span class="service-icon"><svg viewBox="0 0 20 20" aria-hidden="true"><circle cx="8" cy="11" r="3.5"/><circle cx="14.5" cy="6" r="2.2"/></svg></span>
        <span class="service-label">Organisationsmanagement</span>
      </div>
      <div class="service">
        <span class="service-icon"><svg viewBox="0 0 20 20" aria-hidden="true"><circle cx="6" cy="7" r="2.2"/><circle cx="14" cy="7" r="2.2"/><path d="M2 16c0-3 2-4.5 4-4.5s4 1.5 4 4.5M10 16c0-3 2-4.5 4-4.5s4 1.5 4 4.5"/></svg></span>
        <span class="service-label">Vorträge &amp; Seminare</span>
      </div>
    </div>
    <p class="website">www.lukasbrenner.coach</p>
  </section>
</main>
</body>
</html>
```